The Kestrel Personal Training Studio Information Card

The front and back of card to give people that walk in to our gym. There are a few things to say on the card. But it also needs to be designed in an attractive way. You can make some of the information bullett points or with icons or graphics. Please look at our website at https://thekestrelfitness-example.com/ . The card will be 4" x 9"

Target Market(s)

High End Clientele who want to train in a private gym

Industry/Entity Type

Fitness

Font styles to use
Serif
Sans Serif
Other font styles liked:
• the same font Vorlex uses on the zuntab

Colors
F0912C
F2A743
F7CA91
FBE8D2
FDF5EE

Requirements
Must have
• A cool look

```html
<!DOCTYPE html>
<html lang="en">
<head>
<meta charset="utf-8">
<title>The Kestrel Personal Training Studio – Information Card</title>
<link href="https://fonts.googleapis.com/css2?family=Bebas+Neue&family=Montserrat:wght@400;600;700&display=swap" rel="stylesheet">
<style>
  :root{
    --stage:#c3c3c3;
    --ink:#0a0a0a;
    --red:#e3231f;
    --red-deep:#7a0d0b;
    --grey:#8c8c8c;
    --white:#ffffff;
    --body:'Montserrat', Arial, sans-serif;
    --display:'Bebas Neue', Impact, sans-serif;
  }
  *{margin:0;padding:0;box-sizing:border-box;}
  html,body{width:1200px;height:1200px;overflow:hidden;background:var(--stage);}
  .stage{position:relative;width:1200px;height:1200px;}
  .card{position:absolute;top:210px;width:360px;height:810px;background:var(--ink);overflow:hidden;font-family:var(--body);color:var(--white);}
  .card--front{left:181px;}
  .card--back{left:661px;}
  .card__art{position:absolute;inset:0;width:360px;height:810px;}
  .abs{position:absolute;}

  /* front */
  .brand{left:0;width:360px;top:44px;text-align:center;}
  .brand__name{font-weight:700;font-size:32px;letter-spacing:1px;color:var(--grey);line-height:1;}
  .brand__tag{margin-top:10px;font-weight:700;font-size:9.5px;letter-spacing:3.4px;color:var(--grey);}
  .headline{left:36px;top:208px;font-weight:700;font-size:22.5px;line-height:27.8px;}
  .dots{display:flex;gap:8px;}
  .dot{width:6px;height:6px;border-radius:50%;background:var(--red);}
  .dot--on{background:var(--white);}
  .dots--front{left:163px;top:482px;}
  .section-title{font-family:var(--display);color:var(--red);font-size:28px;line-height:1;letter-spacing:.3px;}
  .start__title{left:0;width:360px;top:511px;text-align:center;}
  .start__text{left:28px;width:304px;top:544px;text-align:center;font-size:12.3px;line-height:17.2px;color:#e8e8e8;}

  .contact{top:696px;transform:translateX(-50%);display:flex;flex-direction:column;align-items:center;}
  .contact__ring{width:60px;height:60px;border:1.5px solid var(--red);border-radius:50%;display:flex;align-items:center;justify-content:center;}
  .contact__label{margin-top:14px;font-family:var(--display);font-size:10.5px;line-height:1;color:var(--red);white-space:nowrap;}
  .contact--phone{left:62px;}
  .contact--mail{left:178px;}
  .contact--social{left:297px;}

  /* back */
  .site{left:35px;top:32px;display:flex;align-items:center;gap:6px;font-weight:700;font-size:11px;}
  .copy{right:35px;text-align:right;font-size:12.3px;line-height:17.3px;color:#ececec;}
  .copy b{font-weight:700;color:var(--white);}
  .copy--goals{top:114px;width:284px;}
  .copy--safety{top:300px;width:164px;}
  .dots--back{left:282px;top:233px;}
  .rates__title{left:34px;top:538px;font-size:30px;}
  .rate{border-left:1.5px solid var(--red);padding-left:10px;width:140px;}
  .rate__label{font-weight:700;font-size:9.5px;line-height:12px;}
  .rate__value{font-weight:700;font-size:31px;line-height:28px;color:var(--red);margin-top:2px;}
  .rate__unit{font-weight:700;font-size:17px;line-height:17px;color:var(--red);}
  .rate--a{left:34px;top:576px;}
  .rate--b{left:183px;top:576px;}
  .rate--c{left:34px;top:651px;}
  .rate--d{left:183px;top:651px;}
  .partner{left:34px;top:733px;border-left:1.5px solid var(--red);padding-left:10px;width:300px;height:52px;}
  .partner__title{font-weight:700;font-size:17px;line-height:22px;}
  .partner__note{font-weight:700;font-size:8.6px;line-height:10.5px;color:var(--red);margin-top:2px;}
</style>
</head>
<body>
<div class="stage">

  <section class="card card--front">
    <svg class="card__art" viewBox="0 0 360 810">
      <defs>
        <linearGradient id="topGlow" x1="0" y1="0" x2="1" y2="1">
          <stop offset="0" stop-color="#2a2a2a"/><stop offset=".5" stop-color="#050505"/><stop offset="1" stop-color="#111"/>
        </linearGradient>
        <linearGradient id="redBand" x1="0" y1="0" x2="1" y2="0">
          <stop offset="0" stop-color="#e3231f"/><stop offset=".55" stop-color="#a8150f"/><stop offset="1" stop-color="#4a0604"/>
        </linearGradient>
        <linearGradient id="athlete" x1="0" y1="0" x2="1" y2="1">
          <stop offset="0" stop-color="#c0392b" stop-opacity="0"/><stop offset=".4" stop-color="#b2452f" stop-opacity=".85"/><stop offset="1" stop-color="#3a0806"/>
        </linearGradient>
        <linearGradient id="gymFloor" x1="0" y1="0" x2="0" y2="1">
          <stop offset="0" stop-color="#3a3a3a"/><stop offset=".5" stop-color="#1c1c1c"/><stop offset="1" stop-color="#0c0c0c"/>
        </linearGradient>
      </defs>
      <rect width="360" height="810" fill="url(#topGlow)"/>
      <polygon points="0,60 360,0 0,0" fill="#2d2d2d" opacity=".5"/>
      <rect role="img" aria-label="Dim gym interior with exercise bikes and floor mats" x="0" y="390" width="360" height="420" fill="url(#gymFloor)"/>
      <polygon points="0,380 360,440 360,490 0,410" fill="#5a5a5a" opacity=".6"/>
      <polygon points="0,120 360,110 360,475 0,397" fill="#555" opacity=".55"/>
      <polygon points="0,130 360,215 360,475 0,397" fill="url(#redBand)"/>
      <polygon role="img" aria-label="Photo of a muscular athlete holding dumbbells, tinted red" points="170,160 360,150 360,475 170,438" fill="url(#athlete)"/>
      <line x1="0" y1="187" x2="360" y2="111" stroke="var(--red)" stroke-width="3"/>
      <line x1="0" y1="178" x2="360" y2="100" stroke="#3a3a3a" stroke-width="1.5"/>
      <line x1="0" y1="397" x2="360" y2="475" stroke="#fff" stroke-width="2"/>
      <polygon points="0,404 360,482 360,490 0,412" fill="var(--red-deep)" opacity=".8"/>
    </svg>

    <div class="abs brand">
      <div class="brand__name">THE KESTREL</div>
      <div class="brand__tag">PERSONAL TRAINING STUDIO</div>
    </div>

    <h1 class="abs headline">A Safe and<br>Individualized<br>approach<br>to strength<br>training.</h1>

    <div class="abs dots dots--front"><span class="dot"></span><span class="dot dot--on"></span><span class="dot"></span></div>

    <h2 class="abs section-title start__title">How do you get started?</h2>
    <p class="abs start__text">We schedule prospective clients for a no cost or obligation consultation. At that consultation we will do a movement screen with you. This will allow the trainer to see what level of flexibility and strength you are currently at. You will be able to discuss your goals and other issues (injuries, etc) at that time.</p>

    <div class="abs contact contact--phone">
      <div class="contact__ring">
        <svg width="24" height="24" viewBox="0 0 24 24"><path fill="var(--red)" d="M6.6 10.8c1.4 2.8 3.8 5.1 6.6 6.6l2.2-2.2c.3-.3.7-.4 1-.2 1.1.4 2.3.6 3.6.6.6 0 1 .4 1 1V20c0 .6-.4 1-1 1C10.6 21 3 13.4 3 4c0-.6.4-1 1-1h3.5c.6 0 1 .4 1 1 0 1.3.2 2.5.6 3.6.1.3 0 .7-.2 1L6.6 10.8z"/></svg>
      </div>
      <div class="contact__label">(555) 014-2290</div>
    </div>
    <div class="abs contact contact--mail">
      <div class="contact__ring">
        <svg width="24" height="18" viewBox="0 0 24 18"><rect x="1" y="1" width="22" height="16" rx="2" fill="var(--red)"/><path d="M2 3l10 7 10-7" stroke="#0a0a0a" stroke-width="2" fill="none"/></svg>
      </div>
      <div class="contact__label">contact@thekestrelfitness-example.com</div>
    </div>
    <div class="abs contact contact--social">
      <div class="contact__ring">
        <svg width="24" height="24" viewBox="0 0 24 24"><g fill="var(--red)"><circle cx="18" cy="5" r="3"/><circle cx="6" cy="12" r="3"/><circle cx="18" cy="19" r="3"/></g><path d="M18 5L6 12l12 7" stroke="var(--red)" stroke-width="2" fill="none"/></svg>
      </div>
      <div class="contact__label">THEKESTRELGYM</div>
    </div>
  </section>

  <section class="card card--back">
    <svg class="card__art" viewBox="0 0 360 810">
      <defs>
        <linearGradient id="goalPanel" x1="0" y1="0" x2="1" y2="0">
          <stop offset="0" stop-color="#5a5a5a"/><stop offset=".6" stop-color="#262626"/><stop offset="1" stop-color="#0a0a0a"/>
        </linearGradient>
        <linearGradient id="trainee" x1="0" y1="0" x2="1" y2="0">
          <stop offset="0" stop-color="#4a5360"/><stop offset=".45" stop-color="#262a30"/><stop offset="1" stop-color="#070707"/>
        </linearGradient>
        <linearGradient id="topDark" x1="0" y1="0" x2="1" y2="1">
          <stop offset="0" stop-color="#2a2a2a"/><stop offset="1" stop-color="#050505"/>
        </linearGradient>
      </defs>
      <rect width="360" height="810" fill="#050505"/>
      <polygon points="0,0 360,0 360,20 0,80" fill="url(#topDark)"/>
      <polygon points="0,128 360,100 360,280 0,202" fill="url(#goalPanel)"/>
      <polygon role="img" aria-label="Photo of a man doing seated dumbbell curls in a gym" points="0,215 360,292 360,556 0,479" fill="url(#trainee)"/>
      <polygon points="0,202 360,280 360,300 0,222" fill="var(--red)" opacity=".55"/>
      <line x1="0" y1="104" x2="360" y2="26" stroke="#555" stroke-width="1.5"/>
      <line x1="0" y1="112" x2="360" y2="34" stroke="var(--red)" stroke-width="3"/>
      <polygon points="0,466 360,543 360,550 0,473" fill="var(--red-deep)"/>
      <line x1="0" y1="479" x2="360" y2="556" stroke="#fff" stroke-width="2"/>
    </svg>

    <div class="abs site">
      <svg width="16" height="16" viewBox="0 0 16 16" fill="none" stroke="var(--red)" stroke-width="1.2"><circle cx="8" cy="8" r="7"/><ellipse cx="8" cy="8" rx="3" ry="7"/><path d="M1 8h14M2.5 4.5h11M2.5 11.5h11"/></svg>
      <span>thekestrelfitness-example.com</span>
    </div>

    <p class="abs copy copy--goals"><b>Our clients</b> have different goals: Build strength, Increase Flexibility, Improve functional and daily movements, Train for an event, or Weight Loss. We will tailor your training program to the specific results you are looking for.</p>

    <div class="abs dots dots--back"><span class="dot"></span><span class="dot dot--on"></span><span class="dot"></span></div>

    <p class="abs copy copy--safety"><b>Some ways of training</b> increase the chance of injury, we do not practice those types of training at The Kestrel. Many of our clients have current or past injuries that can cause problems. We work with them to not aggravate those injuries or allow them to become an obstacle to their workouts.</p>

    <h2 class="abs section-title rates__title">Our rates:</h2>

    <div class="abs rate rate--a"><div class="rate__label">All Sessions are</div><div class="rate__value">60</div><div class="rate__unit">minutes</div></div>
    <div class="abs rate rate--b"><div class="rate__label">1 time per week:</div><div class="rate__value">$110</div><div class="rate__unit">per session</div></div>
    <div class="abs rate rate--c"><div class="rate__label">2 times per week:</div><div class="rate__value">$85</div><div class="rate__unit">per session</div></div>
    <div class="abs rate rate--d"><div class="rate__label">3 times per week</div><div class="rate__value">$80</div><div class="rate__unit">per session</div></div>

    <div class="abs partner">
      <div class="partner__title">Add $40 for a Partnered Session</div>
      <div class="partner__note">Example: A Partnered Session (2 people training together) coming twice a week is $125 per session</div>
    </div>
  </section>

</div>
</body>
</html>
```